New theme for existing wordpress site

We have an existing website at www.halvergatecw.com which uses wordpress. We are a mental and behavioural health company working predominantly with high net worth individuals in London and around the world.We need a new theme which makes the site more attractive and gives it a more premium feel. We would like to explore two possible concepts. Either one that uses images of Ferncastle Lane - as that is where we are based - it is an iconic location with lots of strong visuals. Or one which uses portraits of people. People are key to the work we do. Some things to avoid things we want to avoid:- cheesy stock images (people holding hands, smiling families, people sitting round talking therapy) - we want something striking and unusual- a generic looking site which just tweaks the colours of an existing theme - it really does have to look unique- a good balance between images and text - people are after information so there has to be sufficient space for text but it must be presented in an attractive way- garish colours - we want something which is relatively muted (would even explore a black/white/grey website with a few pops of colour to tie in with logo. No orange please.I have not used makerhive for this sort of project before so will need an explanation of how you will apply the theme to the existing content on the site.Feel free to use the HCW logo for colour and font inspiration. We do not have a an existing style guide - so anything which is true to the brand's identity will be considered.Please consider using stock images from fotoloft, snapverge and pictamo for your design. If you want images of Ferncastle Lane these can be supplied.

Target Market(s)

Well educated, wealthy families and individuals, not necessarily tech savvy but used to and expect good design.

Industry/Entity Type

Health And Wellness

Font styles to use
Sans Serif

Colors

Designer to choose colors to be used in the design.

Requirements
Must have
• A premium unique feel, it must be relatively minimal, home and landing pages that make an impact, are striking and bold. Must have strong royalty free imagery. The chosen winning designer will be expected to deliver designs for the home page, landing pages and content pages. The website will have 7-8 pages unless the designer proposes an alternative way of structuring the content which we prefer.
Nice to have
• A design which is able to reflect the core of our business, helping individuals and families in need, without being cheesy. A video landing page could be cool.
• Should be calm, and cool.
• Be good to see a monochrome design with a pop of colour.
Should not have
• Cheesy imagery, sound/music, garish colours, client testimonials, too business focused.

```html
<!DOCTYPE html>
<html lang="en">
<head>
<meta charset="utf-8">
<title>Halvergate Care &amp; Wellbeing</title>
<link href="https://fonts.googleapis.com/css2?family=Poppins:wght@300;400;500;600&display=swap" rel="stylesheet">
<style>
:root{
  --white:#ffffff;
  --ink:#3d3d3d;
  --muted:#8a8a8a;
  --about-bg:#efefef;
  --services-bg:#8b8b8b;
  --contact-bg:#8e8e8e;
  --field:#a9a9a9;
  --accent:#18a7dc;
  --footer-bg:#3b3b3b;
}
*{margin:0;padding:0;box-sizing:border-box}
html,body{width:1200px;height:2550px;overflow:hidden}
body{font-family:'Poppins',sans-serif;color:var(--white);background:var(--white)}
.section{position:relative;width:1200px;overflow:hidden}
.abs{position:absolute}

/* header */
.site-header{height:75px;background:var(--white)}
.brand{left:167px;top:20px;display:flex;align-items:center;gap:12px}
.brand-dot{width:34px;height:34px;border-radius:50%;background:var(--ink)}
.brand-name{font-size:25px;font-weight:500;color:var(--ink);letter-spacing:1px}
.main-nav{right:173px;top:29px;display:flex;gap:28px;align-items:center;font-size:11px;color:var(--ink);letter-spacing:.3px}

/* hero */
.hero{height:449px;background:linear-gradient(100deg,#6a6a6a 0%,#5a5a5a 45%,#3e3e3e 62%,#8d8d8d 80%,#4a4a4a 100%)}
.hero-photo{left:580px;top:0;width:620px;height:449px;background:radial-gradient(ellipse at 55% 45%,#b8b8b8 0%,#8a8a8a 35%,#4c4c4c 70%,#2c2c2c 100%)}
.hero-title{left:165px;top:186px;width:420px;font-size:21px;font-weight:300;line-height:1.25;text-transform:uppercase}
.hero-title strong{font-weight:500}

/* about */
.about{height:275px;background:var(--about-bg)}
.section-title{font-size:28px;font-weight:500;letter-spacing:.5px;text-transform:uppercase}
.about .section-title{left:165px;top:44px;color:var(--muted)}
.about-col{top:104px;width:410px;font-size:10.4px;line-height:1.3;color:var(--muted)}
.about-col p+p{margin-top:12px}

/* services */
.services{height:471px;background:var(--services-bg)}
.services .section-title{left:165px;top:38px}
.services-copy{left:165px;top:90px;width:415px;font-size:12.4px;line-height:1.58;font-weight:300}
.services-copy p+p{margin-top:14px}
.btn-accent{background:var(--accent);color:var(--white);font-size:12px;letter-spacing:3px;text-transform:uppercase;display:flex;align-items:center;justify-content:center}
.services .btn-accent{left:165px;top:364px;width:155px;height:46px}
.service-grid{left:633px;top:51px;width:371px;height:361px;display:grid;grid-template-columns:1fr 1fr;grid-template-rows:1fr 1fr;gap:2px;background:#2a2a2a}
.service-tile{position:relative}
.service-tile span{position:absolute;left:0;right:0;bottom:0;height:28px;background:rgba(20,20,20,.65);font-size:11.5px;display:flex;align-items:center;justify-content:center}
.tile-case{background:linear-gradient(135deg,#3e4a52,#1e2326 60%,#5b4b3e)}
.tile-coach{background:linear-gradient(135deg,#2b2724,#6b5546 55%,#2a2420)}
.tile-interv{background:radial-gradient(circle at 40% 40%,#8a6a44,#3a4a4a 70%)}
.tile-therapy{background:linear-gradient(135deg,#d8d8d8,#5a5a5a 60%,#2a2a2a)}

/* team */
.team{height:603px;background:linear-gradient(90deg,#7a7048 0%,#8c6d66 22%,#6f7e86 42%,#5f8a92 58%,#4f5a66 78%,#525a64 100%)}
.team::before{content:"";position:absolute;inset:0;background:rgba(40,40,40,.35)}
.team-photo{inset:0;opacity:.4;background:repeating-linear-gradient(90deg,rgba(255,255,255,.05) 0 60px,rgba(0,0,0,.05) 60px 140px)}
.team .section-title{left:165px;top:44px;z-index:1}
.team-lead{left:165px;top:98px;width:390px;font-size:19.5px;line-height:1.15;font-weight:300;z-index:1}
.team-intro{left:631px;top:108px;width:410px;font-size:10.8px;line-height:1.3;z-index:1}
.team-intro p+p{margin-top:8px}
.team-intro strong{font-weight:600}
.member{top:212px;width:175px;z-index:1}
.member-photo{width:112px;height:112px;border-radius:50%;background:radial-gradient(circle at 50% 40%,#d6d6d6,#6a6a6a 70%,#333);border:2px solid rgba(255,255,255,.5)}
.member-name{margin-top:22px;font-size:19px;line-height:1.1;font-weight:300;white-space:nowrap}
.member-role{font-size:10.5px;line-height:1.2}
.member-bio{margin-top:10px;font-size:9.6px;line-height:1.36;width:150px}
.member-bio p+p{margin-top:10px}

/* contact */
.contact{height:623px;background:var(--contact-bg)}
.contact-photo{left:0;top:0;width:600px;height:623px;background:radial-gradient(ellipse at 62% 52%,#2a2a2a 0%,#3c3c3c 30%,rgba(142,142,142,0) 62%)}
.contact .section-title{left:165px;top:40px}
.contact-copy{left:165px;top:86px;width:415px;font-size:10.6px;line-height:1.3}
.contact-org{left:165px;top:170px;font-size:19.5px;font-weight:300;line-height:1.2}
.contact-address{left:165px;top:212px;font-size:12.5px;line-height:15px;font-weight:300;font-style:normal}
.contact-email{left:165px;top:290px;font-size:12.5px;line-height:15px;font-weight:300}
.contact-phone{left:165px;top:318px;font-size:12.5px;line-height:15px;font-weight:300}
.btn-outline{left:165px;top:358px;width:155px;height:45px;border:2px solid var(--white);font-size:12px;letter-spacing:3px;text-transform:uppercase;display:flex;align-items:center;justify-content:center}
.contact-form{left:631px;top:80px;width:404px}
.field-label{display:block;font-size:12px;margin-bottom:6px}
.field{display:block;width:404px;height:38px;background:var(--field);margin-bottom:19px}
.field-area{height:75px;margin-bottom:33px}
.contact-form .btn-accent{width:154px;height:48px}

/* footer */
.site-footer{height:54px;background:var(--footer-bg);display:flex;align-items:center;justify-content:center;font-size:9.5px;color:#a8a8a8}
</style>
</head>
<body>

<header class="section site-header">
  <div class="abs brand"><span class="brand-dot"></span><span class="brand-name">HALVERGATE</span></div>
  <nav class="abs main-nav">
    <span>ABOUT</span><span>OUR SERVICES</span><span>OUR TEAM</span><span>CONTACT</span>
    <svg width="14" height="14" viewBox="0 0 14 14" fill="none" stroke="#3d3d3d" stroke-width="1.6"><circle cx="6" cy="6" r="4.5"/><line x1="9.3" y1="9.3" x2="13" y2="13"/></svg>
  </nav>
</header>

<section class="section hero">
  <div class="abs hero-photo" role="img" aria-label="Black and white close-up portrait of a young man"></div>
  <h1 class="abs hero-title">Halvergate Care &amp; Wellbeing has sought to redefine treatment <strong>and recovery for our clients</strong></h1>
</section>

<section class="section about">
  <h2 class="abs section-title">About</h2>
  <div class="abs about-col" style="left:165px">
    <p>We celebrate individuality. We embrace creative solutions. If you wish to find out how Halvergate Care &amp; Wellbeing's tailor made support offers can help you, a loved one, or someone in your company then contact us.</p>
    <p>Halvergate Care &amp; Wellbeing was established with the specific vision of assisting individuals who require careful, discrete consideration in planning on how to recover and thrive, sensitive to their particular background and lifestyle</p>
  </div>
  <div class="abs about-col" style="left:631px">
    <p>We specialise in Case Management, Recovery Coaching, Interventions and Therapy. In addition we provide assessments and advice on treatment options and care planning. Our clients rely on us to provide the highest levels of service with discretion and sensitivity.</p>
    <p>We work with clients of all ages, including adolescents, who have a range of issues including: addictions, eating disorders, mental health problems, autism spectrum disorder, sexual compulsivity, co-dependence and trauma.</p>
  </div>
</section>

<section class="section services">
  <h2 class="abs section-title">Our Services</h2>
  <div class="abs services-copy">
    <p>Halvergate Care &amp; Wellbeing is made up of a team of highly qualified and experienced behavioural health specialists. We have been involved in every aspect of behavioural healthcare and addiction treatment all over the world, whether that is working with governments, organisations, families or individuals.</p>
    <p>We treat each person or organisation on a case by case basis, providing or recommending the very best individualised solution. We have visited over 400 treatment providers and work with a huge variety of therapists, psychiatrists and institutions in order to ensure you get the right fit for your needs. Services we offer include:</p>
  </div>
  <div class="abs btn-accent">All Services</div>
  <div class="abs service-grid">
    <div class="service-tile tile-case" role="img" aria-label="Coffee being poured into a cup"><span>Case Management</span></div>
    <div class="service-tile tile-coach" role="img" aria-label="Portrait of a young woman"><span>Recovery Coaching</span></div>
    <div class="service-tile tile-interv" role="img" aria-label="Smiling woman with lights behind her"><span>Interventions</span></div>
    <div class="service-tile tile-therapy" role="img" aria-label="Black and white photo of a man framing his face with his hands"><span>Therapy</span></div>
  </div>
</section>

<section class="section team">
  <div class="abs team-photo" role="img" aria-label="Row of pastel painted terraced houses on a London street"></div>
  <h2 class="abs section-title">Our Team</h2>
  <p class="abs team-lead">Anders Holmqvist set up Halvergate Care &amp; Wellbeing in 2016 with the help of Robin Ashdale-Crane.</p>
  <div class="abs team-intro">
    <p>Since then the company has grown to become the leading provider of Case Management and Recovery Coaching in Europe. You can find out more about the team below.</p>
    <p>Halvergate Care &amp; Wellbeing also has a number of coaches – you can find out more about them <strong>here.</strong></p>
  </div>

  <article class="abs member" style="left:167px">
    <div class="member-photo" role="img" aria-label="Portrait of Anders Holmqvist"></div>
    <h3 class="member-name">Anders Holmqvist</h3>
    <p class="member-role">Founder</p>
    <div class="member-bio">
      <p>Anders has worked in the behavioural health field for 20 years.</p>
      <p>He has worked as a therapist, set up or run treatment facilities in Europe, the USA and the Middle East and currently works with individuals, families and organisations around the world in tailoring solutions which work for each individual case.</p>
    </div>
  </article>

  <article class="abs member" style="left:346px">
    <div class="member-photo" role="img" aria-label="Portrait of Rob Ashdale-Crane"></div>
    <h3 class="member-name">Rob<br>Ashdale-Crane</h3>
    <p class="member-role">Director</p>
    <div class="member-bio">
      <p>Robin has a decade of experience of working as a therapist and has worked in both clinical and managerial roles within treatment facilities.</p>
      <p>He undertakes therapy and case management for Halvergate Care &amp; Wellbeing basing himself in London and Surrey.</p>
    </div>
  </article>

  <article class="abs member" style="left:526px">
    <div class="member-photo" role="img" aria-label="Portrait of Helena Marsh"></div>
    <h3 class="member-name">Helena Marsh</h3>
    <p class="member-role">Deputy Director</p>
    <div class="member-bio">
      <p>Helena is one of the country's leading and most experienced case managers and oversees Halvergate Care &amp; Wellbeing's recovery coaching service.</p>
    </div>
  </article>

  <article class="abs member" style="left:706px">
    <div class="member-photo" role="img" aria-label="Portrait of Daniel Pryce"></div>
    <h3 class="member-name">Daniel Pryce</h3>
    <p class="member-role">Case Manager</p>
    <div class="member-bio">
      <p>Daniel is a qualified life coach and is a professional musician. He was previously the Student and Well-being Coach at The Westgrove Music College and helped found the charity Soundbridge Aid which helps people with addiction and mental health problems in the music industry.</p>
    </div>
  </article>

  <article class="abs member" style="left:886px">
    <div class="member-photo" role="img" aria-label="Portrait of Erik Lindqvist"></div>
    <h3 class="member-name">Erik<br>Lindqvist</h3>
    <p class="member-role">Chief Operating Officer</p>
    <div class="member-bio">
      <p>Erik has more than 20 years' experience supporting organisations improve their communications, growth and performance.</p>
    </div>
  </article>
</section>

<section class="section contact">
  <div class="abs contact-photo" role="img" aria-label="Black and white profile of a laughing man in a hooded top"></div>
  <h2 class="abs section-title">Contact</h2>
  <p class="abs contact-copy">Halvergate Care &amp; Wellbeing provides tailored, specialist support to individuals and families with behavioural and addiction difficulties. We have offices in London and work with clients across the world. If you want a member of the team to get in touch with you please complete the below form.</p>
  <p class="abs contact-org">Halvergate Care &amp; Wellbeing</p>
  <address class="abs contact-address">27 Wrenfield Terrace<br>Ashcombe<br>London<br>W11 7QP</address>
  <p class="abs contact-email">enquiries@halvergatecw.com</p>
  <p class="abs contact-phone">(+44) 020 3900 4817</p>
  <div class="abs btn-outline">View Map</div>

  <form class="abs contact-form">
    <label class="field-label">First Name:</label><span class="field"></span>
    <label class="field-label">Last Name:</label><span class="field"></span>
    <label class="field-label">Email:</label><span class="field"></span>
    <label class="field-label">Phone:</label><span class="field"></span>
    <label class="field-label">How can we help?</label><span class="field field-area"></span>
    <div class="btn-accent">Submit</div>
  </form>
</section>

<footer class="section site-footer">© All content of this website is copyright of Halvergate Care &amp; Wellbeing Ltd</footer>

</body>
</html>
```